Website for company called VORENTbio

We need a website for our new company called VORENTbio which developed a platform/technology to identify antigen-specific T cells (immune cells) which can be used for cancer therapy, autoimmunity, etc.

The platform is called VORENT and is rapid, versatile, unbiased, and inexpensive.

We have a semi-final logo although we are not completely set on color and font of text (attached).

Target Market(s)

Our target audience at the moment would be potential investors and VCs. We eventually are interested in getting attention from scientists and cell/immunotherapy companies.

Industry/Entity Type

Healthcare/Technology

Coding

Coded - Design and coding required

Number of Pages Required

1 page

Colors
0094D4
00A9DD
6FCCEA
C7EBF8
E9F6FB
00AB8E
00BBA5
67D7C9
C6EFE9
E9F9F6
E54698
E96AAD
F1A4CE
F9D9EA
FCEFF6
A7469A
B969AE
D3A5CF
EDDBEB
F8F0F9
6B429C
8869AF
B7A5CE
E3DAEB
F3F0F8

Requirements
Must have
• Landing page about the company, About us page, Technology page (could be merged with company landing page), Contact us page

```html
<!DOCTYPE html>
<html lang="en">
<head>
<meta charset="utf-8">
<title>vorentbio — Unlocking the Power of the Immune System</title>
<link href="https://fonts.googleapis.com/css2?family=League+Spartan:wght@400;500;600;700&family=Saira:wght@400;600;700&display=swap" rel="stylesheet">
<style>
  :root{
    --blue:#0094D4;
    --sky:#00A9DD;
    --sky-light:#6FCCEA;
    --teal:#00AB8E;
    --teal-mid:#00BBA5;
    --purple:#6B429C;
    --purple-mid:#8869AF;
    --purple-soft:#B7A5CE;
    --lavender:#F3F0F8;
    --ink:#111122;
    --body:#2a2a38;
    --white:#ffffff;
  }
  *{box-sizing:border-box;margin:0;padding:0}
  html,body{width:1200px;height:2895px;overflow:hidden}
  body{font-family:"League Spartan",sans-serif;color:var(--body);background:var(--white);position:relative}
  .abs{position:absolute}

  /* Hero */
  .hero{position:absolute;left:0;top:0;width:1200px;height:710px;overflow:hidden;
    background:radial-gradient(circle at 85% 40%,#5a6fd0 0%,transparent 45%),
               radial-gradient(circle at 60% 75%,#3fa8c8 0%,transparent 40%),
               linear-gradient(120deg,#4a4fb0 0%,#5b56b8 40%,#3b7fc4 70%,#8a78c8 100%)}
  .hero-visual{position:absolute;right:0;top:0;width:720px;height:710px;
    background:radial-gradient(ellipse at 60% 45%,rgba(120,140,230,.55),rgba(70,80,180,.2) 55%,transparent 75%)}
  .hero-wave{position:absolute;left:0;top:700px;width:1200px;height:40px}
  .logo{position:absolute;display:flex;align-items:center;gap:8px;font-family:"League Spartan",sans-serif;font-weight:600;letter-spacing:-.5px}
  .logo-dot{width:22px;height:22px;border-radius:50%}
  .hero .logo{left:98px;top:26px;font-size:38px;color:var(--white)}
  .hero .logo-dot{background:var(--white)}
  .nav{position:absolute;top:38px;display:flex;font-size:16px;font-weight:600;color:var(--white);letter-spacing:.3px}
  .nav a{color:inherit;text-decoration:none}
  .nav-sep{width:1px;height:14px;background:rgba(255,255,255,.5);margin:2px 0}
  .btn-contact{position:absolute;left:942px;top:30px;width:146px;height:39px;border-radius:20px;
    background:linear-gradient(90deg,var(--sky),var(--teal-mid));color:var(--white);font-size:14px;font-weight:600;
    display:flex;align-items:center;justify-content:center;gap:4px}
  .eyebrow-hero{position:absolute;left:108px;top:214px;font-family:"Saira",sans-serif;font-size:22px;letter-spacing:2px;color:var(--white);display:flex;align-items:center;gap:22px}
  .eyebrow-hero span{display:block;width:38px;height:2px;background:var(--sky-light)}
  .hero-title{position:absolute;left:103px;top:250px;font-family:"Saira",sans-serif;color:var(--white);font-size:68px;line-height:60px;letter-spacing:-.5px}
  .hero-title .light{font-weight:400}
  .hero-title .bold{font-weight:700}
  .btn-outline{position:absolute;left:110px;top:460px;width:176px;height:45px;border:2px solid var(--white);border-radius:23px;
    color:var(--white);font-size:15px;font-weight:600;display:flex;align-items:center;justify-content:center;gap:6px}

  /* About */
  .about-backdrop{position:absolute;left:40px;top:740px;width:550px;height:500px;border-radius:50%;
    background:radial-gradient(circle,rgba(0,148,212,.25),rgba(107,66,156,.12) 50%,transparent 70%)}
  .about-visual{position:absolute;left:112px;top:820px;width:425px;height:365px;border-radius:8px;
    background:radial-gradient(circle at 63% 35%,#e86aa8 0%,#6b4fc0 18%,transparent 38%),
               radial-gradient(circle at 25% 75%,#1c7ae0 0%,transparent 40%),
               linear-gradient(135deg,#0a1a6a,#0b2390 55%,#081460)}
  .eyebrow{font-size:19px;font-weight:700;letter-spacing:.3px}
  .about-eyebrow{position:absolute;left:614px;top:827px;color:var(--purple)}
  .about-title{position:absolute;left:610px;top:852px;display:flex;align-items:center;gap:8px;font-size:42px;color:var(--ink)}
  .about-title .light{font-family:"Saira",sans-serif;font-weight:400}
  .about-title .name{font-weight:700;letter-spacing:-1px}
  .about-title .mark{width:22px;height:22px;border-radius:50%;background:var(--purple);margin-left:8px}
  .about-rule{position:absolute;left:1033px;top:874px;width:167px;height:12px}
  .about-text{position:absolute;left:610px;top:927px;width:540px;font-size:17.5px;line-height:26px;color:var(--body)}
  .about-quote{position:absolute;left:608px;top:1058px;width:540px;border-left:2px solid var(--purple-mid);padding-left:17px;font-size:17.5px;line-height:26px;color:var(--body)}

  /* Technology */
  .tech{position:absolute;left:0;top:1335px;width:1200px;height:640px;overflow:hidden;
    background:linear-gradient(120deg,#1a8ac0 0%,#0aa3a8 55%,#00ab8e 100%)}
  .tech-visual{position:absolute;left:606px;top:-105px;width:1060px;height:1060px;border-radius:50%;border:5px solid var(--white);
    background:radial-gradient(circle at 32% 50%,#3aa0f0 0%,#1360d0 18%,#0a3ea8 40%,#0a2a80 70%)}
  .tech-eyebrow{position:absolute;left:102px;top:124px;color:var(--white)}
  .tech-line{position:absolute;left:0;top:167px;width:88px;height:12px}
  .tech-title{position:absolute;left:100px;top:148px;font-family:"Saira",sans-serif;font-size:44px;color:var(--white);display:flex;align-items:center;gap:6px}
  .tech-title .light{font-weight:400}
  .tech-title .bold{font-weight:700}
  .tech-title .mark{width:20px;height:20px;border-radius:50%;background:var(--white);margin-left:6px}
  .tech-text{position:absolute;left:103px;width:480px;font-size:20px;line-height:26.5px;color:var(--white)}

  /* Contact */
  .contact-bg{position:absolute;left:0;top:1975px;width:1200px;height:727px;
    background:radial-gradient(circle at 3% 10%,rgba(233,106,173,.15),transparent 25%),
               radial-gradient(circle at 97% 88%,rgba(111,204,234,.25),transparent 25%),var(--white)}
  .contact-card{position:absolute;left:136px;top:2080px;width:921px;height:528px;border-radius:18px;overflow:hidden;
    background:radial-gradient(circle at 25% 45%,rgba(120,90,200,.55),transparent 45%),
               linear-gradient(125deg,#6b42b0 0%,#4f58c0 45%,#3b7fd0 80%,#3f9ad4 100%)}
  .contact-mark{position:absolute;left:450px;top:22px;width:20px;height:20px;border-radius:50%;background:var(--white)}
  .contact-eyebrow{position:absolute;left:0;width:100%;top:64px;text-align:center;font-family:"Saira",sans-serif;color:var(--white);font-size:17px;letter-spacing:3px}
  .contact-title{position:absolute;left:0;width:100%;top:84px;text-align:center;font-family:"Saira",sans-serif;color:var(--white);font-size:43px}
  .contact-title .bold{font-weight:700}
  .field{position:absolute;background:var(--white);border-radius:3px;display:flex;align-items:center;gap:10px;padding-left:19px;font-size:17px;color:#333}
  .field svg{flex:none}
  .field.message{align-items:flex-start;padding-top:18px}
  .btn-send{position:absolute;left:349px;top:435px;width:204px;height:48px;border-radius:24px;background:#4a2a8a;color:var(--white);
    font-size:15px;font-weight:600;display:flex;align-items:center;justify-content:center;gap:7px}

  /* Footer */
  .footer{position:absolute;left:0;top:2702px;width:1200px;height:193px;background:linear-gradient(90deg,#e8ecf7,#ece6f4 60%,#f0e8f4)}
  .footer .logo{left:120px;top:50px;font-size:38px;color:var(--ink)}
  .footer .logo-dot{background:var(--ink)}
  .footer-nav{position:absolute;top:52px;display:flex;font-size:18px;font-weight:600;color:var(--ink)}
  .footer-rule{position:absolute;left:0;top:118px;width:1200px;height:1px;background:#c9c3de}
  .copyright{position:absolute;left:124px;top:143px;font-size:14px;color:var(--body)}
  .social{position:absolute;top:142px;display:flex;gap:7px;left:919px}
  .social span{width:35px;height:35px;border-radius:50%}
</style>
</head>
<body>

<header class="hero">
  <div class="hero-visual" role="img" aria-label="Photo of a blue DNA double helix beside an immune cell, with soft bokeh light"></div>
  <div class="logo"><span class="logo-dot"></span>vorentbio</div>
  <nav class="nav" style="left:517px;gap:26px">
    <a href="#home">HOME</a><span class="nav-sep"></span>
    <a href="#about">ABOUT</a><span class="nav-sep"></span>
    <a href="#technology">TECHNOLOGY</a>
  </nav>
  <div class="btn-contact">CONTACT US
    <svg width="8" height="10" viewBox="0 0 8 10"><path d="M2 1l4 4-4 4" fill="none" stroke="#fff" stroke-width="1.6"/></svg>
  </div>
  <p class="eyebrow-hero">WELCOME TO VORENTBIO <span></span></p>
  <h1 class="hero-title"><span class="light">Unlocking the</span><br><span class="bold">Power of the<br>Immune System</span></h1>
  <div class="btn-outline">LEARN MORE
    <svg width="8" height="10" viewBox="0 0 8 10"><path d="M2 1l4 4-4 4" fill="none" stroke="#fff" stroke-width="1.6"/></svg>
  </div>
</header>

<svg class="hero-wave" viewBox="0 0 1200 40" aria-hidden="true">
  <path d="M0 10 H380 C420 10 440 2 470 8 C500 14 520 32 545 24 C570 16 580 -4 615 10 C640 20 650 34 670 28 C700 18 720 0 760 8 C790 14 810 10 840 10 H1200" fill="none" stroke="var(--sky-light)" stroke-width="3"/>
</svg>

<section id="about">
  <div class="about-backdrop" aria-hidden="true"></div>
  <div class="about-visual" role="img" aria-label="Illustration of a glowing blue cell targeted by a crosshair, symbolising antigen-specific T cell detection"></div>
  <p class="eyebrow about-eyebrow">WHO WE ARE</p>
  <h2 class="about-title"><span class="light">About</span><span class="name">vorentbio</span><span class="mark"></span></h2>
  <svg class="about-rule" viewBox="0 0 167 12" aria-hidden="true"><circle cx="6" cy="6" r="5" fill="var(--purple-mid)"/><line x1="14" y1="6" x2="167" y2="6" stroke="var(--purple-mid)" stroke-width="1.5"/></svg>
  <p class="about-text">Lorem ipsum dolor sit amet, consectetur adipiscing elit, sed do eiusmod tempor incididunt ut labore et dolore magna aliqua. Ut enim ad minim veniam, quis nostrud exercitation ullamco laboris nisi ut aliquip ex ea commodo consequat.</p>
  <p class="about-quote">Duis aute irure dolor in reprehenderit in voluptate velit esse cillum dolore eu fugiat nulla pariatur. Excepteur sint occaecat cupidatat non proident, sunt in culpa qui officia deserunt mollit anim id est laborum.Sed ut perspiciatis unde omnis iste</p>
</section>

<section class="tech" id="technology">
  <div class="tech-visual" role="img" aria-label="Microscope-style image of a blue immune cell surrounded by a molecular network"></div>
  <p class="eyebrow tech-eyebrow">OUR TECHNOLOGY</p>
  <svg class="tech-line" viewBox="0 0 88 12" aria-hidden="true"><line x1="0" y1="6" x2="78" y2="6" stroke="#fff" stroke-width="1.5"/><circle cx="82" cy="6" r="5" fill="#fff"/></svg>
  <h2 class="tech-title"><span class="light">How</span> <span class="bold">VORENT Works</span><span class="mark"></span></h2>
  <p class="tech-text" style="top:220px">Lorem ipsum dolor sit amet, consectetur adipiscing elit, sed do eiusmod tempor incididunt ut labore et dolore magna aliqua. Ut enim ad minim veniam, quis nostrud exercitation ullamco laboris nisi ut</p>
  <p class="tech-text" style="top:351px">Duis aute irure dolor in reprehenderit in voluptate velit esse cillum dolore eu fugiat nulla pariatur. Excepteur sint occaecat cupidatat non proident, sunt in culpa qui officia deserunt mollit ani</p>
</section>

<section id="contact">
  <div class="contact-bg" aria-hidden="true"></div>
  <div class="contact-card">
    <span class="contact-mark"></span>
    <p class="contact-eyebrow">GET IN TOUCH</p>
    <h2 class="contact-title">Contact <span class="bold">Us</span></h2>

    <div class="field" style="left:92px;top:153px;width:366px;height:53px">
      <svg width="16" height="16" viewBox="0 0 16 16"><circle cx="8" cy="5" r="3.5" fill="#9aa0b8"/><path d="M1 16c0-4 3-6 7-6s7 2 7 6z" fill="#9aa0b8"/></svg>First Name</div>
    <div class="field" style="left:471px;top:153px;width:366px;height:53px">
      <svg width="16" height="16" viewBox="0 0 16 16"><circle cx="8" cy="5" r="3.5" fill="#9aa0b8"/><path d="M1 16c0-4 3-6 7-6s7 2 7 6z" fill="#9aa0b8"/></svg>Last Name</div>
    <div class="field" style="left:91px;top:217px;width:366px;height:53px">
      <svg width="18" height="13" viewBox="0 0 18 13"><rect x="0" y="0" width="18" height="13" rx="1.5" fill="#9aa0b8"/><path d="M1 1l8 6 8-6" fill="none" stroke="#fff" stroke-width="1.3"/></svg>Email address</div>
    <div class="field" style="left:471px;top:217px;width:366px;height:53px">
      <svg width="16" height="16" viewBox="0 0 16 16"><path d="M3 1l3 3-2 2c1 2 3 4 5 5l2-2 3 3-2 3C7 15 1 9 1 3z" fill="#9aa0b8"/></svg>Phone Number</div>
    <div class="field message" style="left:91px;top:284px;width:748px;height:127px">
      <svg width="17" height="15" viewBox="0 0 17 15"><ellipse cx="8.5" cy="6.5" rx="8" ry="6" fill="#9aa0b8"/><path d="M3 10l-2 5 5-3z" fill="#9aa0b8"/></svg>Leave Message</div>

    <div class="btn-send">SEND MESSAGE
      <svg width="8" height="10" viewBox="0 0 8 10"><path d="M2 1l4 4-4 4" fill="none" stroke="#fff" stroke-width="1.6"/></svg>
    </div>
  </div>
</section>

<footer class="footer">
  <div class="logo"><span class="logo-dot"></span>vorentbio</div>
  <nav class="footer-nav" style="left:477px;gap:67px">
    <span>HOME</span><span>ABOUT</span><span>TECHNOLOGY</span><span>CONTACT US</span>
  </nav>
  <div class="footer-rule"></div>
  <p class="copyright">© 2025 vorentbio | All Rights Reserved</p>
  <div class="social" aria-label="Social links">
    <span style="background:var(--purple)"></span>
    <span style="background:var(--sky)"></span>
    <span style="background:var(--purple-mid)"></span>
  </div>
</footer>

</body>
</html>
```